Build Your Own Shake Menu Design

- will be printed on countertop acrylic menu stands that are a foot by a foot

Files:
- document attached for the menu contents
*file name: SHAKEMENU
- sample menu images (these are giant acrylic menu boards that are in my shop)
*file name: newest shave ice menu, newest spi rolls menu (JPG)
-picture of the shop where the menus will be placed
*file name: shop (PNG)

```html
<!DOCTYPE html>
<html lang="en">
<head>
<meta charset="utf-8">
<title>Create Your Own Shake Menu</title>
<link rel="stylesheet" href="https://fonts.googleapis.com/css2?family=Lilita+One&family=Pacifico&family=Rye&family=Pinyon+Script&family=Kaushan+Script&family=Montserrat:wght@400;600;700;800&family=Lobster&display=swap">
<style>
:root{
  --sky:#cfe6f5;
  --sky-deep:#9fcbe8;
  --navy:#132a57;
  --blue:#1f5fb0;
  --blue-light:#3f8fd8;
  --red:#c8102e;
  --red-dark:#9e0d22;
  --pink:#e88a8f;
  --ink:#1b1b1b;
  --white:#ffffff;
  --grey:#e9edf1;
  --gold:#e6c229;
  --purple:#8a4fb8;
  --magenta:#e0339a;
  --orange:#f08a2b;
}
*{box-sizing:border-box;margin:0;padding:0}
html,body{width:1200px;height:900px;overflow:hidden;background:#e4e4e4}
.menu{position:relative;width:1200px;height:900px;display:flex}
.panel{position:relative;width:400px;height:900px;overflow:hidden;
  background:linear-gradient(160deg,#e3f1fa 0%,var(--sky) 45%,var(--sky-deep) 100%);
  border-right:1px solid #b7d3e6}
.panel:last-child{border-right:none}
.abs{position:absolute}

/* ---------- panel 1 ---------- */
.title-card{left:45px;top:50px;width:310px;height:230px;background:var(--navy);
  transform:rotate(-3deg);border:4px solid var(--blue-light);box-shadow:8px 8px 0 var(--pink)}
.title-card .line{display:block;text-align:center;font-family:'Lilita One',sans-serif;line-height:1}
.title-create{color:var(--pink);font-size:34px;margin-top:18px}
.title-your{color:var(--white);font-size:34px}
.title-shake{color:#f0566a;font-size:50px}
.title-menu{color:var(--white);font-family:'Pacifico',cursive !important;font-size:62px;margin-top:-8px;text-shadow:3px 3px 0 var(--blue)}

.band{left:20px;width:360px;background:linear-gradient(90deg,var(--blue-light),var(--navy));
  clip-path:polygon(4% 0,100% 0,96% 100%,0 100%);color:var(--white);text-align:center}
.band-base{top:305px;height:64px}
.band-base .head{font-family:'Rye',serif;font-size:24px;padding-top:6px}
.band-base .sub{font-family:'Pinyon Script',cursive;font-size:22px;line-height:1}
.band-special{top:452px;height:54px}
.band-special .head{font-family:'Pinyon Script',cursive;font-size:30px;text-align:left;padding:6px 0 0 55px}
.badge{width:70px;height:70px;border-radius:50%;background:var(--white);border:5px solid #9aa7b5;
  display:flex;flex-direction:column;align-items:center;justify-content:center;color:var(--navy)}
.badge b{font-family:'Montserrat',sans-serif;font-weight:800;font-size:24px;line-height:1}
.badge small{font-family:'Montserrat',sans-serif;font-size:8px}
.badge-base{left:260px;top:445px}

.flavors{left:0;width:400px;text-align:center;font-family:'Rye',serif;color:var(--red);
  font-size:30px;text-shadow:1px 1px 0 var(--white),2px 2px 0 var(--navy)}
.flavors .dot{display:inline-block;width:22px;height:10px;border-radius:50%;background:var(--gold);margin:0 6px;vertical-align:middle;transform:rotate(-20deg)}
.flavors-std{top:400px}
.flavors-sp1{top:518px}
.flavors-sp2{top:556px}

.band-add{top:598px;left:20px;width:360px;height:46px;background:linear-gradient(90deg,var(--blue),var(--blue-light));
  text-align:center;color:var(--white)}
.band-add .head{font-family:'Lobster',cursive;color:var(--gold);font-size:18px;padding-top:3px}
.band-add .sub{font-family:'Lobster',cursive;font-size:14px;line-height:1}

.additions{left:20px;top:650px;width:360px;list-style:none}
.additions li{height:23.5px;font-family:'Montserrat',sans-serif;font-weight:600;font-size:12px;
  color:var(--ink);text-align:center;line-height:20px;background:var(--white);
  border-bottom:3px solid var(--pink);white-space:nowrap}

/* ---------- panel 2 ---------- */
.free-oval{left:18px;top:18px;width:170px;height:100px;border-radius:50%;background:var(--white);border-right:5px solid var(--blue)}
.free-word{left:30px;top:8px;font-family:'Kaushan Script',cursive;color:var(--red);font-size:70px;transform:rotate(-8deg)}
.art{border-radius:10px}
.art-topping{left:250px;top:20px;width:130px;height:110px;border-radius:50% 50% 20px 20px;
  background:linear-gradient(180deg,#f0a548,#c9752a 60%,#5a1a1a)}
.whip{left:150px;top:108px;font-family:'Montserrat',sans-serif;font-weight:700;font-size:20px}
.cream{left:15px;top:125px;font-family:'Montserrat',sans-serif;font-weight:700;font-size:52px;color:var(--white);
  -webkit-text-stroke:2px var(--blue);letter-spacing:1px}
.and-a{left:228px;top:142px;font-family:'Montserrat',sans-serif;font-weight:800;font-size:30px;color:var(--ink)}
.cherry{left:140px;top:172px;font-family:'Montserrat',sans-serif;font-weight:800;font-size:48px;color:var(--red)}
.to-every{left:140px;top:222px;font-family:'Montserrat',sans-serif;font-weight:600;font-size:17px}
.milkshake{left:15px;top:230px;font-family:'Kaushan Script',cursive;font-size:66px;color:var(--red);
  text-shadow:2px 2px 0 var(--white),4px 4px 0 var(--navy)}

.tag{display:flex;align-items:center;height:36px}
.tag .price{background:var(--white);border-radius:18px;padding:6px 10px;font-family:'Montserrat',sans-serif;
  font-weight:800;font-size:16px;color:var(--red);box-shadow:1px 2px 3px rgba(0,0,0,.25);position:relative;z-index:1}
.tag .label{margin-left:-10px;background:linear-gradient(#fff,var(--grey));border-right:6px solid var(--red);
  clip-path:polygon(0 0,100% 0,94% 100%,0 100%);padding:3px 18px 3px 20px;
  font-family:'Montserrat',sans-serif;font-style:italic;font-weight:600;font-size:10px;color:#667;line-height:1.15;text-align:center}
.tag-drink .label{font-size:14px;padding:7px 20px 7px 18px;min-width:105px}
.t1{left:15px;top:318px}.t2{left:205px;top:318px}
.t3{left:15px;top:448px}.t4{left:205px;top:448px}
.photo-cups{left:70px;top:360px;width:105px;height:82px;border-radius:8px;background:linear-gradient(160deg,#f4e3cf,#b5604c)}
.photo-sundae{left:260px;top:360px;width:95px;height:82px;border-radius:8px;background:linear-gradient(160deg,#f4e3cf,#7a2626)}

.band-drinks{top:500px;left:15px;width:370px;height:40px;background:linear-gradient(90deg,var(--blue-light),var(--navy));
  clip-path:polygon(0 0,100% 0,97% 100%,3% 100%);text-align:center;color:var(--white);
  font-family:'Rye',serif;font-size:22px;line-height:40px}
.d1{left:15px;top:560px}.d2{left:15px;top:630px}.d3{left:15px;top:700px}
.d4{left:210px;top:700px}.d5{left:15px;top:770px}
.d5 .label{min-width:170px;padding:3px 20px 3px 18px;line-height:1.15}
.photo-drinks{left:200px;top:550px;width:180px;height:135px;background:linear-gradient(120deg,#dff2ff,#c4132b 45%,#2c9e3c 85%)}
.photo-bottles{left:250px;top:760px;width:130px;height:70px;background:linear-gradient(90deg,#e07a1c,#d12d2d 45%,#2b5fb5)}

/* ---------- panel 3 ---------- */
.art-kids{left:40px;top:15px;width:320px;height:125px;border-radius:60px 60px 8px 8px;
  background:linear-gradient(90deg,#f6d84a,#a7d56c 50%,#6b3b2a)}
.spoon-board{left:30px;top:140px;width:340px;height:400px;background:linear-gradient(160deg,#ffffff,#d9ecf8);
  border:8px solid var(--blue);box-shadow:6px 6px 0 var(--navy)}
.band-spoons{left:12px;top:18px;width:300px;height:40px;background:linear-gradient(90deg,var(--blue),var(--blue-light));
  clip-path:polygon(4% 0,100% 0,96% 100%,0 100%);color:var(--white);font-family:'Rye',serif;font-size:16px;
  text-align:center;line-height:40px}
.spoons{left:20px;top:80px;width:290px;font-family:'Rye',serif;font-size:26px}
.spoons .row{display:flex;align-items:center;height:44px}
.spoons .from{width:110px}
.spoons .eq{width:40px;color:var(--ink)}
.c-white{color:#fff;text-shadow:1px 1px 0 var(--blue),-1px -1px 0 var(--blue)}
.c-pink{color:var(--magenta)}
.c-blue{color:var(--blue)}
.c-purple{color:var(--purple)}
.c-confetti{color:var(--orange)}
.art-spoons{left:30px;top:230px;width:270px;height:130px;border-radius:6px;
  background:linear-gradient(135deg,#f7d3e6,#d7e2f4 40%,#8a4fb8 70%,#f0a030)}
.badge-spoon{left:190px;top:300px;width:125px;height:125px;border-radius:50%;background:var(--white);
  border:8px solid var(--blue);display:flex;align-items:center;justify-content:center;flex-direction:column}
.badge-spoon .ring{font-family:'Montserrat',sans-serif;font-weight:700;font-size:7px;color:var(--navy);text-align:center;line-height:1.1;padding:0 8px}
.badge-spoon .coin{width:66px;height:66px;border-radius:50%;background:var(--red);color:var(--white);
  display:flex;flex-direction:column;align-items:center;justify-content:center;margin-top:3px}
.badge-spoon .coin b{font-family:'Montserrat',sans-serif;font-weight:800;font-size:26px;line-height:1}
.badge-spoon .coin small{font-family:'Lobster',cursive;font-size:11px}
.swoosh{left:0;top:545px;width:400px;height:40px}
.art-balloons{left:160px;top:590px;width:200px;height:95px;border-radius:12px;
  background:linear-gradient(135deg,#c9dcef,#b7c8e4)}
.dessert-frame{left:45px;top:690px;width:320px;height:180px;background:var(--navy);border:6px solid var(--blue);
  transform:rotate(-2deg);box-shadow:-8px 8px 0 var(--pink)}
.art-dessert{left:14px;top:14px;width:280px;height:140px;border-radius:4px;
  background:linear-gradient(90deg,#3a1a2a,#5a2a3a 40%,#f48fb1 70%,#d81b3a)}
</style>
</head>
<body>
<main class="menu">

  <section class="panel panel-build">
    <svg class="abs" style="left:0;top:30px" width="400" height="280" aria-hidden="true">
      <polygon points="20,40 70,40 40,260" fill="var(--pink)"/>
      <polygon points="330,20 395,30 360,260" fill="var(--pink)"/>
      <line x1="345" y1="10" x2="380" y2="270" stroke="var(--gold)" stroke-width="3"/>
    </svg>
    <div class="abs title-card">
      <span class="line title-create">Create</span>
      <span class="line title-your">Your Own</span>
      <span class="line title-shake">Shake</span>
      <span class="line title-menu">menu</span>
    </div>

    <div class="abs band band-base">
      <div class="head">CHOOSE YOUR BASE</div>
      <div class="sub">Standard Base</div>
    </div>
    <div class="abs flavors flavors-std">Vanilla<span class="dot"></span>Chocolate</div>

    <div class="abs band band-special"><div class="head">Specialty Bases</div></div>
    <div class="abs badge badge-base"><b>.50</b><small>Cent</small></div>

    <div class="abs flavors flavors-sp1">Mint<span class="dot"></span>Strawberry</div>
    <div class="abs flavors flavors-sp2">Espresso<span class="dot"></span>Cheesecake</div>

    <div class="abs band-add">
      <div class="head">Choose Up To 2 Items For Your Shake</div>
      <div class="sub">Additions Choice</div>
    </div>
    <ul class="abs additions">
      <li>Cookie Dough-Peanut Butter Cup-Butter Crunch</li>
      <li>Alpine Mint-Toffee Bits-Chip Cookies-Graham Crackers</li>
      <li>Cream Cookies-Chocolate Chips-White Chocolate Chips</li>
      <li>Rainbow Sprinkles-Cupcake Bites-Candy Gems</li>
      <li>Nuts-Almonds-Strawberries-Banana-Cherries</li>
      <li>Captain Crisp-Cinnamon Squares</li>
      <li>Fruity Flakes-Cocoa Flakes</li>
      <li>Peanut Butter Drizzle-Chocolate Drizzle</li>
      <li>Strawberry Drizzle-Raspberry Drizzle</li>
      <li>Marshmallow Drizzle</li>
    </ul>
  </section>

  <section class="panel panel-prices">
    <div class="abs free-oval"></div>
    <div class="abs free-word">free</div>
    <div class="abs art art-topping" role="img" aria-label="Whipped cream swirl topped with cherries"></div>
    <div class="abs whip">Whip</div>
    <div class="abs cream">CREAM</div>
    <div class="abs and-a">&amp; A</div>
    <div class="abs cherry">CHERRY</div>
    <div class="abs to-every">to every</div>
    <div class="abs milkshake">Milkshake</div>

    <div class="abs tag t1"><span class="price">$5.75</span><span class="label">15 Ounce<br>Regular</span></div>
    <div class="abs tag t2"><span class="price">$6.25</span><span class="label">15 Ounce<br>Specialty Base</span></div>
    <div class="abs photo-cups" role="img" aria-label="Photo of ice cream cups with toppings"></div>
    <div class="abs photo-sundae" role="img" aria-label="Photo of tall chocolate sundaes"></div>
    <div class="abs tag t3"><span class="price">$5.99</span><span class="label">18 Ounce<br>Large</span></div>
    <div class="abs tag t4"><span class="price">$6.49</span><span class="label">18 Ounce<br>Specialty Base</span></div>

    <div class="abs band-drinks">DRINKS</div>
    <div class="abs art photo-drinks" role="img" aria-label="Photo of bottled water, cola and lemon-lime soda"></div>
    <div class="abs tag tag-drink d1"><span class="price">$1.00</span><span class="label">Water</span></div>
    <div class="abs tag tag-drink d2"><span class="price">$1.99</span><span class="label">Cola</span></div>
    <div class="abs tag tag-drink d3"><span class="price">$1.99</span><span class="label">Lemon-Lime</span></div>
    <div class="abs tag tag-drink d4"><span class="price">$1.99</span><span class="label">Tea</span></div>
    <div class="abs tag tag-drink d5"><span class="price">$1.99</span><span class="label">Sport Drink<br>Fruit Punch</span></div>
    <div class="abs art photo-bottles" role="img" aria-label="Photo of sport drink bottles"></div>
  </section>

  <section class="panel panel-spoons">
    <div class="abs art art-kids" role="img" aria-label="Illustration of three cartoon kids holding the sign"></div>
    <div class="abs spoon-board">
      <div class="abs band-spoons">COLOR CHANGING SPOONS</div>
      <div class="abs spoons">
        <div class="row"><span class="from c-white">White</span><span class="eq">=</span><span class="to c-blue">Blue</span></div>
        <div class="row"><span class="from c-pink">Pink</span><span class="eq">=</span><span class="to c-purple">Purple</span></div>
        <div class="row"><span class="from c-white">White</span><span class="eq">=</span><span class="to c-confetti">Confetti</span></div>
      </div>
      <div class="abs art-spoons" role="img" aria-label="Colorful plastic spoons over a geometric square pattern"></div>
      <div class="abs badge-spoon">
        <div class="ring">COLOR CHANGING SPOONS IN 3 COLORS</div>
        <div class="coin"><b>.50</b><small>Cent</small></div>
      </div>
    </div>
    <svg class="abs swoosh" viewBox="0 0 400 40" aria-hidden="true">
      <path d="M0 35 Q200 -10 400 20" fill="none" stroke="var(--orange)" stroke-width="6"/>
      <path d="M0 28 Q200 -18 400 10" fill="none" stroke="var(--blue)" stroke-width="4"/>
    </svg>
    <div class="abs art-balloons" role="img" aria-label="Illustration of colorful party balloons"></div>
    <div class="abs dessert-frame">
      <div class="abs art-dessert" role="img" aria-label="Photo of chocolate ice cream and a strawberry splashing into pink milk"></div>
    </div>
  </section>

</main>
</body>
</html>
```